KLT Business cards

I currently have a logo that was designed by a sketch harbor designer. I would like this to be added to the business card.

We are an innovative new start-up business offering finance solutions to the car dealership market in the UK. So our clients are quiet traditional, so are cards need to fit in, but at the same time show we are a modern online business.

Industry/Entity Type

Finance

```html
<!DOCTYPE html>
<html lang="en">
<head>
<meta charset="utf-8">
<title>KLT Motor Finance – Business Cards</title>
<link href="https://fonts.googleapis.com/css2?family=Oswald:wght@500&family=Montserrat:wght@400;500&display=swap" rel="stylesheet">
<style>
  :root {
    --navy: #0b2a4f;
    --silver: #b6bdbf;
    --white: #ffffff;
    --backdrop: #8a8a8a;
    --icon-bg: #c3c8cc;
    --text-light: #e8edf3;
  }
  * { margin: 0; padding: 0; box-sizing: border-box; }
  html, body { width: 1200px; height: 904px; overflow: hidden; }
  body {
    background: var(--backdrop);
    font-family: "Montserrat", sans-serif;
    position: relative;
  }
  .card {
    position: absolute;
    top: 122px;
    width: 380px;
    height: 660px;
    background: var(--white);
    overflow: hidden;
    box-shadow: 0 10px 24px rgba(0,0,0,0.35);
  }
  .card--front { left: 180px; }
  .card--back { left: 640px; }
  .band-top { position: absolute; top: 0; left: 0; right: 0; height: 22px; background: var(--silver); }

  /* front */
  .front-panel { position: absolute; top: 22px; left: 0; right: 0; height: 448px; background: var(--navy); }
  .front-divider { position: absolute; top: 470px; left: 0; right: 0; height: 22px; background: var(--silver); }
  .name-tab { position: absolute; top: 88px; left: 0; width: 18px; height: 46px; background: var(--silver); }
  .person { position: absolute; top: 80px; left: 34px; color: var(--white); }
  .person__name { font-family: "Oswald", sans-serif; font-weight: 500; font-size: 32px; letter-spacing: 0.5px; line-height: 1; }
  .person__role { font-size: 13px; letter-spacing: 2px; margin-top: 6px; }
  .contacts { position: absolute; top: 238px; left: 34px; list-style: none; }
  .contacts li { display: flex; align-items: center; height: 34px; color: var(--text-light); font-size: 13px; letter-spacing: 0.6px; white-space: nowrap; }
  .contacts svg { width: 22px; height: 22px; margin-right: 10px; flex: none; }

  /* logo lockup */
  .lockup { position: absolute; left: 0; right: 0; display: flex; align-items: center; justify-content: center; gap: 12px; }
  .card--front .lockup { top: 492px; height: 168px; }
  .card--back .lockup { top: 22px; height: 398px; }
  .lockup__mark { width: 64px; height: 64px; border-radius: 50%; border: 4px solid var(--navy); flex: none; }
  .lockup__name { color: var(--navy); font-weight: 500; font-size: 26px; line-height: 1.05; }

  /* back */
  .back-panel { position: absolute; top: 420px; left: 0; right: 0; bottom: 0; background: var(--navy); }
  .back-web { position: absolute; top: 548px; left: 0; right: 0; text-align: center; color: var(--white); font-size: 15px; letter-spacing: 1px; }
</style>
</head>
<body>
  <section class="card card--front">
    <div class="band-top"></div>
    <div class="front-panel"></div>
    <div class="name-tab"></div>
    <div class="person">
      <div class="person__name">MARA ELLISON</div>
      <div class="person__role">GENERAL MANAGER</div>
    </div>
    <ul class="contacts">
      <li><svg viewBox="0 0 22 22"><rect width="22" height="22" rx="4" fill="var(--icon-bg)"/><path d="M7 5l3 3-1.5 1.5a8 8 0 0 0 4 4L14 12l3 3-2 2c-5 0-10-5-10-10z" fill="var(--navy)"/></svg>020 7946 0321</li>
      <li><svg viewBox="0 0 22 22"><rect width="22" height="22" rx="4" fill="var(--icon-bg)"/><rect x="7" y="4" width="8" height="14" rx="1.5" fill="var(--navy)"/><rect x="8.5" y="6" width="5" height="8" fill="var(--icon-bg)"/></svg>07700 900 418</li>
      <li><svg viewBox="0 0 22 22"><rect width="22" height="22" rx="4" fill="var(--icon-bg)"/><rect x="5" y="9" width="12" height="7" rx="1" fill="var(--navy)"/><rect x="7.5" y="5" width="7" height="4" fill="var(--navy)"/><rect x="7.5" y="14" width="7" height="4" fill="var(--white)"/></svg>020 7946 0322</li>
      <li><svg viewBox="0 0 22 22"><rect width="22" height="22" rx="4" fill="var(--icon-bg)"/><rect x="4" y="6" width="14" height="10" fill="var(--navy)"/><path d="M4 6l7 6 7-6" stroke="var(--icon-bg)" stroke-width="1.3" fill="none"/></svg>mara@kltmotor.co.uk</li>
      <li><svg viewBox="0 0 22 22"><rect width="22" height="22" rx="4" fill="var(--icon-bg)"/><circle cx="11" cy="11" r="6.5" fill="none" stroke="var(--navy)" stroke-width="1.6"/><ellipse cx="11" cy="11" rx="2.8" ry="6.5" fill="none" stroke="var(--navy)" stroke-width="1.3"/><path d="M4.5 11h13" stroke="var(--navy)" stroke-width="1.3"/></svg>www.kltmotorfinance.co.uk</li>
      <li><svg viewBox="0 0 22 22"><rect width="22" height="22" rx="4" fill="var(--icon-bg)"/><path d="M11 4a5 5 0 0 0-5 5c0 4 5 9 5 9s5-5 5-9a5 5 0 0 0-5-5z" fill="var(--navy)"/><circle cx="11" cy="9" r="2" fill="var(--icon-bg)"/></svg>27 Harbour Row, 4th Floor, Leeds LS1</li>
    </ul>
    <div class="front-divider"></div>
    <div class="lockup">
      <span class="lockup__mark"></span>
      <span class="lockup__name">KLT Motor<br>Finance</span>
    </div>
  </section>

  <section class="card card--back">
    <div class="band-top"></div>
    <div class="lockup">
      <span class="lockup__mark"></span>
      <span class="lockup__name">KLT Motor<br>Finance</span>
    </div>
    <div class="back-panel"></div>
    <div class="back-web">www.kltmotorfinance.co.uk</div>
  </section>
</body>
</html>
```